Graphic Design Project

i need Demo graphics designed for my Restaurant App. The app name "TableLoop Plus".
This a Demo app to show potential restaurant owners to try to get them to buy. With the app you can view restaurant men us, specials and events. Post Fanwall and reviews. Alot of other options.
I need the main screen and icons created with the TableLoop Plus logo created. I also need the Specials page created that i will use for the events page also. Also need the reviews page created that i will use for the fanwall page also.
I also need a menu page designed and to match the theme.
I uploaded a few sample screenshots of the current app design.
Updates

Payment is now Guarantee.

Project Deadline Extended
Reason: Need more time for submissions

Hi Do you plan on submitting an updated design soon?

Target Market(s)

restaurant owners. trying to sell them the app.

Industry/Entity Type

Restaurant

Requirements
Must have
• background of something nice that represent a a restaurant but not specific to any one type pf food. Maybe like spoon and fork design or something.
Nice to have
• different icons that represent the different buttons.
eye catching design.
ease of use buttons.

```html
<!DOCTYPE html>
<html lang="en">
<head>
<meta charset="utf-8">
<title>TableLoop Plus – Home</title>
<link rel="stylesheet" href="https://fonts.googleapis.com/css2?family=Kaushan+Script&display=swap">
<style>
  :root {
    --bg-deep: #2a1a10;
    --bg-mid: #6b4a33;
    --bg-light: #a88363;
    --band-dark: #1c120b;
    --band-mid: #3b2717;
    --gold: #e9c46a;
    --gold-light: #fbe7a1;
    --gold-dark: #9a7431;
    --pill-dark: #0d0d0d;
    --pill-mid: #2e2e2e;
    --icon-ring: #cfcfcf;
    --icon-fill: #111;
    --icon-ink: #ffffff;
    --name-ink: #f3ead8;
  }
  * { box-sizing: border-box; margin: 0; padding: 0; }
  html, body { width: 799px; height: 1200px; overflow: hidden; background: #000; }
  .screen {
    position: relative;
    width: 799px; height: 1200px; overflow: hidden;
    background: radial-gradient(ellipse at 50% 55%, var(--bg-light) 0%, var(--bg-mid) 45%, var(--bg-deep) 100%);
    font-family: "Kaushan Script", cursive;
  }
  .band-edge { position: absolute; left: 0; width: 799px; }
  .band-edge.top { top: 0; height: 150px; }
  .band-edge.bottom { bottom: 0; height: 140px; }
  .logo {
    position: absolute; left: 0; top: 62px; width: 799px; text-align: center;
  }
  .logo-name {
    display: inline-block;
    font-family: "Kaushan Script", cursive;
    font-weight: 400;
    font-size: 76px; line-height: 1.1;
    color: var(--name-ink);
  }
  .fork-art {
    position: absolute; left: 320px; top: 300px; width: 158px; height: 860px;
    background: linear-gradient(90deg, #6e4a1f 0%, #f4d79a 35%, #fff3cf 50%, #c89a4c 70%, #5a3a14 100%);
    border-radius: 30px 30px 20px 20px;
    opacity: 0.9;
  }
  .ornament-art {
    position: absolute; width: 190px; height: 300px; opacity: 0.25;
    background: radial-gradient(ellipse at center, var(--gold-light) 0%, transparent 70%);
  }
  .ornament-art.left { left: -20px; top: 260px; }
  .ornament-art.right { right: -20px; top: 260px; }
  .nav-button {
    position: absolute; width: 270px; height: 80px;
    text-decoration: none;
  }
  .nav-label {
    position: absolute; left: 38px; top: 15px; right: 0; height: 52px;
    border: 3px solid var(--gold-dark);
    border-radius: 8px 26px 26px 8px;
    background: linear-gradient(180deg, var(--pill-mid) 0%, var(--pill-dark) 55%, #000 100%);
    color: var(--gold);
    font-size: 31px; line-height: 44px;
    text-align: center; padding-left: 40px;
    white-space: nowrap;
  }
  .nav-icon {
    position: absolute; left: 0; top: 0; width: 80px; height: 80px;
    border-radius: 50%;
    background: var(--icon-fill);
    border: 5px solid var(--icon-ring);
    box-shadow: 0 0 0 2px #000;
    display: flex; align-items: center; justify-content: center;
  }
  .nav-icon svg { width: 46px; height: 46px; }
  .col-left { left: 36px; }
  .col-right { left: 470px; }
  .row-1 { top: 400px; } .row-2 { top: 520px; } .row-3 { top: 642px; }
  .row-4 { top: 764px; } .row-5 { top: 884px; }
</style>
</head>
<body>
<main class="screen">
  <svg class="band-edge top" viewBox="0 0 799 150" preserveAspectRatio="none" aria-hidden="true">
    <rect x="0" y="0" width="799" height="30" fill="#000"/>
    <path d="M0 30 H799 V80 Q400 140 0 80 Z" fill="var(--band-dark)"/>
    <path d="M0 80 Q400 140 799 80" fill="none" stroke="var(--gold)" stroke-width="5"/>
  </svg>
  <div class="ornament-art left" role="img" aria-label="Gold filigree scroll ornament"></div>
  <div class="ornament-art right" role="img" aria-label="Gold filigree scroll ornament"></div>
  <div class="fork-art" role="img" aria-label="Large polished gold fork standing upright"></div>
  <svg class="band-edge bottom" viewBox="0 0 799 140" preserveAspectRatio="none" aria-hidden="true">
    <path d="M0 60 Q400 -10 799 60 V140 H0 Z" fill="var(--band-dark)"/>
    <path d="M0 60 Q400 -10 799 60" fill="none" stroke="var(--gold)" stroke-width="5"/>
  </svg>

  <header class="logo">
    <h1 class="logo-name">TableLoop Plus</h1>
  </header>

  <nav>
    <a class="nav-button col-left row-1" href="#menu">
      <span class="nav-label">Menu</span>
      <span class="nav-icon"><svg viewBox="0 0 48 48"><path d="M8 32 A16 16 0 0 1 40 32 Z" fill="var(--icon-ink)"/><rect x="4" y="34" width="40" height="4" rx="2" fill="var(--icon-ink)"/><circle cx="24" cy="13" r="3" fill="var(--icon-ink)"/></svg></span>
    </a>
    <a class="nav-button col-left row-2" href="#directions">
      <span class="nav-label">Directions</span>
      <span class="nav-icon"><svg viewBox="0 0 48 48"><rect x="9" y="9" width="30" height="30" rx="4" transform="rotate(45 24 24)" fill="none" stroke="var(--icon-ink)" stroke-width="4"/><path d="M19 30 V22 H28 M24 17 L29 22 L24 27" fill="none" stroke="var(--icon-ink)" stroke-width="4"/></svg></span>
    </a>
    <a class="nav-button col-left row-3" href="#gallery">
      <span class="nav-label">Gallery</span>
      <span class="nav-icon"><svg viewBox="0 0 48 48"><rect x="6" y="12" width="36" height="26" rx="5" fill="none" stroke="var(--icon-ink)" stroke-width="4"/><circle cx="24" cy="25" r="7" fill="none" stroke="var(--icon-ink)" stroke-width="4"/><rect x="16" y="7" width="12" height="6" fill="var(--icon-ink)"/></svg></span>
    </a>
    <a class="nav-button col-left row-4" href="#fanwall">
      <span class="nav-label">Fanwall</span>
      <span class="nav-icon"><svg viewBox="0 0 48 48"><rect x="6" y="6" width="24" height="28" fill="var(--icon-ink)"/><rect x="16" y="14" width="26" height="28" fill="var(--icon-fill)" stroke="var(--icon-ink)" stroke-width="4"/></svg></span>
    </a>
    <a class="nav-button col-left row-5" href="#events">
      <span class="nav-label">Events</span>
      <span class="nav-icon"><svg viewBox="0 0 48 48"><rect x="4" y="14" width="30" height="18" rx="2" transform="rotate(-15 19 23)" fill="var(--icon-ink)"/><rect x="12" y="20" width="30" height="18" rx="2" fill="var(--icon-fill)" stroke="var(--icon-ink)" stroke-width="3"/></svg></span>
    </a>

    <a class="nav-button col-right row-1" href="#specials">
      <span class="nav-label">Specials</span>
      <span class="nav-icon"><svg viewBox="0 0 48 48"><circle cx="24" cy="24" r="10" fill="none" stroke="var(--icon-ink)" stroke-width="4"/><g stroke="var(--icon-ink)" stroke-width="4"><path d="M24 2V10M24 38V46M2 24H10M38 24H46M8 8L14 14M34 34L40 40M40 8L34 14M14 34L8 40"/></g></svg></span>
    </a>
    <a class="nav-button col-right row-2" href="#reviews">
      <span class="nav-label">Reviews</span>
      <span class="nav-icon"><svg viewBox="0 0 48 48"><path d="M10 4H30L38 12V44H10Z" fill="var(--icon-ink)"/><g stroke="var(--icon-fill)" stroke-width="3"><path d="M15 18H33M15 25H33M15 32H28"/></g><circle cx="32" cy="34" r="6" fill="var(--icon-fill)" stroke="var(--icon-ink)" stroke-width="3"/></svg></span>
    </a>
    <a class="nav-button col-right row-3" href="#fancircle">
      <span class="nav-label">FanCircle</span>
      <span class="nav-icon"><svg viewBox="0 0 48 48"><circle cx="24" cy="24" r="16" fill="var(--icon-ink)"/></svg></span>
    </a>
    <a class="nav-button col-right row-4" href="#polls">
      <span class="nav-label">Polls</span>
      <span class="nav-icon"><svg viewBox="0 0 48 48"><g fill="var(--icon-ink)"><rect x="6" y="20" width="7" height="22"/><rect x="16" y="10" width="7" height="32"/><rect x="26" y="16" width="7" height="26"/><rect x="36" y="26" width="7" height="16"/></g></svg></span>
    </a>
    <a class="nav-button col-right row-5" href="#more">
      <span class="nav-label">More</span>
      <span class="nav-icon"><svg viewBox="0 0 48 48"><path d="M18 6H30V18H42V30H30V42H18V30H6V18H18Z" fill="var(--icon-ink)"/></svg></span>
    </a>
  </nav>
</main>
</body>
</html>
```